Awesome new bottle needs Awesome new label

We need an awesome label design for our new bottle. It is a square bottle with 4 flat surfaces for the label. These surfaces make it easier to play with transparent labels.
The water comes from the Mount Kelvara Springs. Themes that we want to concentrate on are purity of the water as well as the clarity of the bottle. Think Quenor's new label design for inspiration. I am looking for something like that. I have attached pictures of the bottle as well as the schematics of the label.
The brand to be used is "Brumelle", which means Solar in French. I would like transparent labels as the smooth surfaces make good areas to play with this idea.
Thanks and good luck!
Tav
Reason: Waiting for the final designs from my shortlisted designers

```html
<!DOCTYPE html>
<html lang="en">
<head>
<meta charset="utf-8">
<title>Brumelle Natural Mineral Water – Label</title>
<link rel="stylesheet" href="https://fonts.googleapis.com/css2?family=Tenor+Sans&display=swap">
<style>
  :root{
    --ink:#2b4aa6;
    --sun:#f28c1e;
    --bg-centre:#eef3ff;
    --bg-edge:#bccffb;
    --paper:#ffffff;
    --frame:#9aaee0;
  }
  *{margin:0;padding:0;box-sizing:border-box}
  html,body{width:1200px;height:1000px;overflow:hidden}
  body{
    position:relative;
    background:radial-gradient(ellipse 620px 520px at 790px 490px,var(--bg-centre) 0%,#d6e2fd 55%,var(--bg-edge) 100%);
    font-family:"Tenor Sans","Gill Sans",sans-serif;
    color:var(--ink);
    font-size:10.5px;
    letter-spacing:.06em;
  }
  .label-sheet{
    position:absolute;left:95px;top:520px;width:1017px;height:191px;
    background:var(--paper);
    box-shadow:0 2px 6px rgba(40,60,120,.25);
  }
  .label{position:absolute;width:930px;height:170px}
  .label--clear{left:147px;top:245px}
  .label--white{left:142px;top:530px}

  .brand-mark{position:absolute;display:flex;align-items:center;gap:6px}
  .brand-mark__dot{border-radius:50%;background:var(--sun);flex:none}
  .brand-mark__name{color:var(--ink);font-family:"Tenor Sans",sans-serif;line-height:1}
  .brand-mark--small{left:8px;top:24px}
  .brand-mark--small .brand-mark__dot{width:18px;height:18px}
  .brand-mark--small .brand-mark__name{font-size:32px;letter-spacing:.02em}
  .brand-mark--main{left:462px;top:52px;width:232px;justify-content:center}
  .brand-mark--main .brand-mark__dot{width:24px;height:24px}
  .brand-mark--main .brand-mark__name{font-size:40px;letter-spacing:.01em}

  .data-table{position:absolute;width:181px;line-height:15px}
  .data-table__title{font-size:11px;letter-spacing:.08em;white-space:nowrap}
  .data-table__row{display:flex;justify-content:space-between}
  .data-table--nutrition{left:0;top:95px}
  .data-table--minerals{left:242px;top:5px}

  .volume{position:absolute;left:628px;top:17px;font-size:10.5px}
  .product-type{position:absolute;left:462px;top:127px;width:232px;text-align:center;font-size:14px;line-height:15px;letter-spacing:.1em}

  .maker{position:absolute;left:716px;top:5px;width:150px;line-height:15px}
  .maker p + p{margin-top:15px}
  .recycle{position:absolute;left:821px;top:141px;width:22px;height:22px}

  .barcode-area{
    position:absolute;left:861px;top:11px;width:64px;height:149px;
    border:1px solid var(--frame);
    display:flex;align-items:center;justify-content:center;
  }
  .barcode-area span{transform:rotate(-90deg);white-space:nowrap;font-size:13px;letter-spacing:.1em}
</style>
</head>
<body>

<div class="label-sheet"></div>

<!-- Two label versions share one structure: clear film and white stock -->
<section class="label label--clear">
  <div class="brand-mark brand-mark--small"><span class="brand-mark__dot"></span><span class="brand-mark__name">Brumelle</span></div>
  <div class="data-table data-table--nutrition">
    <div class="data-table__title">NUTRITIONAL INFORMATION</div>
    <div class="data-table__row"><span>Energy</span><span>0kcal</span></div>
    <div class="data-table__row"><span>Protein</span><span>0g</span></div>
    <div class="data-table__row"><span>Total Fat</span><span>0g</span></div>
    <div class="data-table__row"><span>Carbohydrates</span><span>0g</span></div>
  </div>
  <div class="data-table data-table--minerals">
    <div class="data-table__title">MINERAL COMPOSITION (MG/L)</div>
    <div class="data-table__row"><span>Bicarbonates</span><span>103.0</span></div>
    <div class="data-table__row"><span>Calcium</span><span>8.9</span></div>
    <div class="data-table__row"><span>Sodium</span><span>18.0</span></div>
    <div class="data-table__row"><span>Chlorides</span><span>&lt;3.2</span></div>
    <div class="data-table__row"><span>Sulphates</span><span>11.1</span></div>
    <div class="data-table__row"><span>Magnesium</span><span>10.0</span></div>
    <div class="data-table__row"><span>Potassium</span><span>1.60</span></div>
    <div class="data-table__row"><span>PH at Source</span><span>7.72</span></div>
    <div class="data-table__row"><span>Total Dissolved</span><span>144</span></div>
    <div class="data-table__row"><span>Solids at 180°C</span><span></span></div>
  </div>
  <div class="volume">500ML</div>
  <div class="brand-mark brand-mark--main"><span class="brand-mark__dot"></span><span class="brand-mark__name">Brumelle</span></div>
  <div class="product-type">NATURAL<br>MINERAL WATER</div>
  <div class="maker">
    <p>Manufactured for and imported by:<br>Harlow Waters Pte Ltd,<br>27 Linden Quay Road,<br>Singapore 049312<br>TEL: +65 61074528</p>
    <p>Sourced and bottled at the Mount Kelvara Springs, Indonesia.</p>
  </div>
  <svg class="recycle" viewBox="0 0 24 24" aria-label="Recyclable"><g fill="none" stroke="var(--ink)" stroke-width="2.4" stroke-linejoin="round"><path d="M9 5.5 12 2l3 4.5"/><path d="M19.5 11 21 17h-5"/><path d="M7 20H3l2.5-5.5"/><path d="M12 2 8 9"/><path d="M21 17l-4-6.5"/><path d="M3 20h8"/></g></svg>
  <div class="barcode-area"><span>BARCODE AREA</span></div>
</section>

<section class="label label--white">
  <div class="brand-mark brand-mark--small"><span class="brand-mark__dot"></span><span class="brand-mark__name">Brumelle</span></div>
  <div class="data-table data-table--nutrition">
    <div class="data-table__title">NUTRITIONAL INFORMATION</div>
    <div class="data-table__row"><span>Energy</span><span>0kcal</span></div>
    <div class="data-table__row"><span>Protein</span><span>0g</span></div>
    <div class="data-table__row"><span>Total Fat</span><span>0g</span></div>
    <div class="data-table__row"><span>Carbohydrates</span><span>0g</span></div>
  </div>
  <div class="data-table data-table--minerals">
    <div class="data-table__title">MINERAL COMPOSITION (MG/L)</div>
    <div class="data-table__row"><span>Bicarbonates</span><span>103.0</span></div>
    <div class="data-table__row"><span>Calcium</span><span>8.9</span></div>
    <div class="data-table__row"><span>Sodium</span><span>18.0</span></div>
    <div class="data-table__row"><span>Chlorides</span><span>&lt;3.2</span></div>
    <div class="data-table__row"><span>Sulphates</span><span>11.1</span></div>
    <div class="data-table__row"><span>Magnesium</span><span>10.0</span></div>
    <div class="data-table__row"><span>Potassium</span><span>1.60</span></div>
    <div class="data-table__row"><span>PH at Source</span><span>7.72</span></div>
    <div class="data-table__row"><span>Total Dissolved</span><span>144</span></div>
    <div class="data-table__row"><span>Solids at 180°C</span><span></span></div>
  </div>
  <div class="volume">500ML</div>
  <div class="brand-mark brand-mark--main"><span class="brand-mark__dot"></span><span class="brand-mark__name">Brumelle</span></div>
  <div class="product-type">NATURAL<br>MINERAL WATER</div>
  <div class="maker">
    <p>Manufactured for and imported by:<br>Harlow Waters Pte Ltd,<br>27 Linden Quay Road,<br>Singapore 049312<br>TEL: +65 61074528</p>
    <p>Sourced and bottled at the Mount Kelvara Springs, Indonesia.</p>
  </div>
  <svg class="recycle" viewBox="0 0 24 24" aria-label="Recyclable"><g fill="none" stroke="var(--ink)" stroke-width="2.4" stroke-linejoin="round"><path d="M9 5.5 12 2l3 4.5"/><path d="M19.5 11 21 17h-5"/><path d="M7 20H3l2.5-5.5"/><path d="M12 2 8 9"/><path d="M21 17l-4-6.5"/><path d="M3 20h8"/></g></svg>
  <div class="barcode-area"><span>BARCODE AREA</span></div>
</section>

</body>
</html>
```